Spectacular Business Card Design for AI SAAS Plattform called Pathleap.ai

Hi Creators
I need an outstanding new Design for my business card.
I run an AI automated Saas Plattform Called Pathleap.ai

Front side:
Logo
Slogan: DIY Business Development & Social Media Management
Data:
Name: Markus Velbringer - CEO / Founder
email: m.velbringer@pathleap-example.ai
mobile: +43 699 82 37 915

Company name:
Pathleap FlexCo

Backside:

What we stand for Slogan:
Vertrauen in KI-Technologie, getragen von menschlicher Vision: Dein Sprung nach vorn!
+ a fancy design what captures our core competencies - AI automisations, Social Media Management, Business development
(dont know if its too much, but AI and social media should be )

pls find attached the logo and the old design

Industry/Entity Type

AI automations for marketing and business development

Contact Information for Business Card

Front side: Logo Slogan: DIY Business Development & Social Media Management Data: Name: Markus Velbringer - CEO / Founder email: m.velbringer@pathleap-example.ai mobile: +43 699 82 37 915 Company name: Pathleap FlexCo Backside: What we stand for Slogan: Vertrauen in KI-Technologie, getragen von menschlicher Vision: Dein Sprung nach vorn!

Font styles to use
Serif
Sans Serif

Requirements
Nice to have
• a fancy design on the backside, a fancy design what captures our core competencies - AI automisations, Social Media Management, Business development

```html
<!DOCTYPE html>
<html lang="en">
<head>
<meta charset="utf-8">
<title>Pathleap.ai Business Card</title>
<link href="https://fonts.googleapis.com/css2?family=Poppins:wght@400;500;600;700&display=swap" rel="stylesheet">
<style>
  :root {
    --teal: #0f87a4;
    --teal-deep: #0a6f88;
    --teal-light: #16b6d8;
    --orange: #f08a2c;
    --ink: #2a2f33;
    --muted: #6b7378;
    --paper: #ffffff;
    --mist: #f1f2f3;
    --stage: #d6d6d6;
  }
  * { box-sizing: border-box; margin: 0; padding: 0; }
  html, body {
    width: 1200px; height: 800px; overflow: hidden;
    background: var(--stage);
    font-family: "Poppins", sans-serif;
  }
  .stage {
    position: relative; width: 1200px; height: 800px;
    display: flex; align-items: center; justify-content: center; gap: 50px;
  }
  .card {
    position: relative; width: 530px; height: 303px;
    border-bottom: 3px solid var(--orange);
    box-shadow: 0 10px 24px rgba(0,0,0,.18);
    overflow: hidden;
  }

  /* Front */
  .card-front { background: var(--paper); }
  .brand-glow {
    position: absolute; right: 0; top: 0; width: 250px; height: 303px;
    background: linear-gradient(200deg, var(--mist) 0%, rgba(241,242,243,0) 75%);
  }
  .brand-mark {
    position: absolute; left: 40px; top: 118px;
    display: flex; align-items: center; gap: 10px;
  }
  .brand-square { width: 24px; height: 24px; background: var(--orange); flex: none; }
  .brand-name {
    font-size: 32px; font-weight: 600; color: var(--teal); letter-spacing: .3px; line-height: 1;
  }
  .contact {
    position: absolute; left: 252px; top: 62px; width: 262px;
  }
  .person-name { font-size: 21px; font-weight: 600; color: var(--teal); line-height: 1.15; white-space: nowrap; }
  .person-name .surname { color: var(--orange); }
  .person-role { font-size: 13.5px; color: var(--ink); margin-top: 3px; }
  .divider { width: 40px; height: 2px; background: var(--orange); margin: 14px 0; }
  .contact-line {
    display: flex; align-items: center; gap: 8px;
    font-size: 12px; color: var(--ink); margin-bottom: 6px; white-space: nowrap;
  }
  .contact-line svg { width: 13px; height: 13px; flex: none; }
  .company {
    margin-top: 12px; font-size: 11.5px; font-weight: 500; color: var(--muted); letter-spacing: .3px;
  }

  /* Back */
  .card-back { background: var(--teal); }
  .back-pattern {
    position: absolute; inset: 0;
    background: linear-gradient(135deg, var(--teal-deep) 0%, var(--teal) 55%, var(--teal-light) 100%);
  }
  .back-claim {
    position: absolute; left: 26px; top: 26px; width: 300px;
    font-size: 12.5px; font-weight: 500; line-height: 1.45; color: var(--paper);
  }
  .back-claim .claim-accent { color: var(--orange); font-weight: 600; }
  .back-sign {
    position: absolute; right: 26px; bottom: 30px; text-align: right; color: var(--paper);
  }
  .back-brand {
    display: inline-flex; align-items: center; gap: 6px;
    font-size: 16px; font-weight: 600; margin-bottom: 8px;
  }
  .back-brand .brand-square { width: 12px; height: 12px; }
  .slogan { font-size: 15px; font-weight: 600; line-height: 1.25; }
</style>
</head>
<body>
<main class="stage">
  <section class="card card-front" aria-label="Card front">
    <div class="brand-glow" role="img" aria-label="Faint brand decoration area"></div>
    <div class="brand-mark">
      <span class="brand-square"></span>
      <span class="brand-name">Pathleap</span>
    </div>
    <div class="contact">
      <p class="person-name">Markus <span class="surname">Velbringer</span></p>
      <p class="person-role">CEO / Founder</p>
      <div class="divider"></div>
      <p class="contact-line">
        <svg viewBox="0 0 16 16" aria-hidden="true"><path fill="#0f87a4" d="M3.6 1.5l2.3 2.7-1.3 1.6c.9 2 2.6 3.7 4.6 4.6l1.6-1.3 2.7 2.3-1.4 2.1C6.6 13.3 2.7 9.4 1.5 3z"/></svg>
        +43 699 82 37 915
      </p>
      <p class="contact-line">
        <svg viewBox="0 0 16 16" aria-hidden="true"><rect x="1" y="3" width="14" height="10" fill="#0f87a4"/><path d="M1.5 3.5L8 9l6.5-5.5" fill="none" stroke="#fff" stroke-width="1.3"/></svg>
        m.velbringer@pathleap-example.ai
      </p>
      <p class="company">Pathleap FlexCo</p>
    </div>
  </section>

  <section class="card card-back" aria-label="Card back">
    <div class="back-pattern" role="img" aria-label="Repeating pattern expressing AI automation, social media management and business development, in teal tones"></div>
    <p class="back-claim">Vertrauen in KI-Technologie, getragen von menschlicher Vision: <span class="claim-accent">Dein Sprung nach vorn!</span></p>
    <div class="back-sign">
      <div class="back-brand"><span class="brand-square"></span>Pathleap</div>
      <p class="slogan">DIY Business Development &amp;<br>Social MediaManagement</p>
    </div>
  </section>
</main>
</body>
</html>
```